Flyer-Design für Wohn -und Einrichtungsberaterin
Zielgruppe
Ich bin eine Wohn -und Einrichtungsberaterin und biete neben der Wohnraumopitimierung auch Gartenberatung und Workshops an. Ich bin gelernte Floristin und habe daher einen engen Bezug zur Natürlichkeit.
Aufgabenstellung
Mein Flyer soll die Größe 148 x 148mm haben, mit einer klaren und ruhigen Erscheinung. Das Farbkonzept sollte sich in natürlichen und gedeckten Erdtönen wiederfinden. Trotzdem soll das Konzept ausdrucksstark präsentiert werden.
Vorderseite:
-transparentes Wohnbild im Hintergrund, darauf das Logo
-Bild (Tisch) und Logo siehe Anhänge
Rückseite:
-4 quadratische Textwürfel 2x2 angeordnet (neben- und untereinander)
1. Würfel (oben links)
Überschrift: WOHNRAUMGESTALTUNG
Text: Mit der vorhandenen Einrichtung eine Verbesserung des Wohngefühls schaffen.
2. Würfel (oben rechts)
Überschrift:GARTENBERATUNG
Text: Durch Anregung in der Garten -und Terassengestaltung ein neues Erscheinungsbild kreieren.
3. Würfel (unten links)
Überschrift: RAUMDESIGN
Text: In Praxis- und Gewerberäumen eine neue Atmosphäre erzielen.
4.Würfel (unten rechts)
Überschrift: WORKSHOPS
Text: Kreative Gruppenevents zu verschiedensten Anlässen und Themen erleben.

```html
<!DOCTYPE html>
<html lang="de">
<head>
<meta charset="utf-8">
<title>Lebensart – Flyer</title>
<link rel="stylesheet" href="https://fonts.googleapis.com/css2?family=Montserrat:wght@300;400&family=EB+Garamond:wght@400&display=swap">
<style>
  :root {
    --paper: #ffffff;
    --photo-light: #ece6df;
    --photo-warm: #d9cabb;
    --photo-cool: #c9cfc8;
    --sage-light: #9ba298;
    --sage-dark: #7f857a;
    --tile: rgba(255, 255, 255, 0.16);
    --line: #ffffff;
    --ink: #3b4341;
  }
  * { margin: 0; padding: 0; box-sizing: border-box; }
  html, body { width: 1200px; height: 599px; overflow: hidden; background: var(--paper); }
  .canvas { position: relative; width: 1200px; height: 599px; }

  .front {
    position: absolute; left: 93px; top: 49px; width: 509px; height: 509px;
    overflow: hidden;
  }
  .front-photo {
    position: absolute; inset: 0;
    background:
      radial-gradient(ellipse at 85% 25%, #f3f1ea 0%, transparent 45%),
      radial-gradient(ellipse at 40% 20%, var(--photo-cool) 0%, transparent 55%),
      linear-gradient(170deg, #cbbfb4 0%, var(--photo-warm) 45%, var(--photo-light) 100%);
  }
  .logo-frame {
    position: absolute; left: 91px; top: 325px; width: 327px; height: 117px;
    border: 1px solid var(--line);
  }
  .logo-plate {
    position: absolute; left: 100px; top: 334px; width: 310px; height: 100px;
    background: var(--paper);
    display: flex; align-items: center; justify-content: center;
  }
  .brand-name {
    font-family: "Montserrat", sans-serif; font-weight: 300;
    font-size: 34px; letter-spacing: 3px; color: var(--ink);
  }

  .back {
    position: absolute; left: 617px; top: 49px; width: 510px; height: 509px;
    background: linear-gradient(90deg, var(--sage-light) 0%, #8f968b 55%, var(--sage-dark) 100%);
    overflow: hidden;
  }
  .back-frame {
    position: absolute; left: 16px; top: 16px; width: 477px; height: 477px;
    border: 1px solid var(--line);
  }
  .tile {
    position: absolute; width: 188px; height: 188px;
    background: var(--tile);
    color: var(--line);
  }
  .tile--living { left: 49px; top: 44px; }
  .tile--garden { left: 271px; top: 44px; }
  .tile--space  { left: 49px; top: 277px; }
  .tile--events { left: 271px; top: 277px; }

  .tile-title {
    position: absolute; left: 25px; top: 37px;
    font-family: "Montserrat", sans-serif; font-weight: 300;
    font-size: 14px; line-height: 17px; letter-spacing: 1.8px;
    text-transform: uppercase;
  }
  .tile-text {
    position: absolute; left: 24px; top: 86px; width: 160px;
    font-family: "EB Garamond", serif; font-size: 12px; line-height: 17px;
  }
  .tile--space .tile-title, .tile--events .tile-title { top: 29px; }
  .tile--space .tile-text, .tile--events .tile-text { top: 55px; }

  .accent-frame {
    position: absolute; left: 278px; top: 36px; width: 189px; height: 189px;
    border: 1px solid var(--line);
  }
  .accent-square {
    position: absolute; border: 1px solid var(--line);
  }
  .accent-square--large { left: 202px; top: 196px; width: 46px; height: 46px; }
  .accent-square--small { left: 68px; top: 419px; width: 21px; height: 21px; }
</style>
</head>
<body>
<div class="canvas">
  <section class="front">
    <div class="front-photo" role="img" aria-label="Transparentes Wohnbild: Holztisch mit Stühlen, Windlichtern und Vasen"></div>
    <div class="logo-frame"></div>
    <div class="logo-plate"><span class="brand-name">Lebensart</span></div>
  </section>

  <section class="back">
    <div class="back-frame"></div>

    <div class="tile tile--living">
      <h2 class="tile-title">Wohnraum-<br>gestaltung</h2>
      <p class="tile-text">Mit der vorhandenen<br>Einrichtung eine Verbesse-<br>rung des Wohngefühls<br>schaffen.</p>
    </div>
    <div class="tile tile--garden">
      <h2 class="tile-title">Garten-<br>beratung</h2>
      <p class="tile-text">Durch Anregung in der<br>Garten- und Terassen-<br>gestaltung ein neues<br>Erscheinungsbild kreieren.</p>
    </div>
    <div class="tile tile--space">
      <h2 class="tile-title">Raumdesign</h2>
      <p class="tile-text">In Praxis- und Gewerberäu-<br>men eine neue Atmosphäre<br>erzielen.</p>
    </div>
    <div class="tile tile--events">
      <h2 class="tile-title">Workshops</h2>
      <p class="tile-text">Kreative Gruppenevents<br>zu verschiedensten Anlässen<br>und Themen erleben.</p>
    </div>

    <div class="accent-frame"></div>
    <div class="accent-square accent-square--large"></div>
    <div class="accent-square accent-square--small"></div>
  </section>
</div>
</body>
</html>
```